The Quiet Hour Safeguard Handbook

A book cover. The book will be marketed as a promotional item for financial advisors, financial planners, independent insurance agents, bankers, and any professional who views their role as guardian of their clients assets and helping them manage risk.

```html
<!DOCTYPE html>
<html lang="en">
<head>
<meta charset="UTF-8">
<title>The Quiet Hour Safeguard Handbook — Cover</title>
<link rel="stylesheet" href="https://fonts.googleapis.com/css2?family=Oswald:wght@600;700&family=Montserrat:wght@600;700;800;900&display=swap">
<style>
  :root {
    --backdrop: #c4c4c4;
    --navy-deep: #06112a;
    --navy: #0d1f45;
    --navy-light: #1a3670;
    --gold: #d9a93f;
    --gold-light: #f6d57e;
    --gold-dark: #9c7226;
    --white: #ffffff;
    --ink: #0a0f1e;
  }
  * { margin: 0; padding: 0; box-sizing: border-box; }
  html, body { width: 857px; height: 1200px; overflow: hidden; background: var(--backdrop); }
  .cover {
    position: absolute; left: 61px; top: 20px; width: 735px; height: 1160px;
    background: radial-gradient(ellipse at 50% 60%, var(--navy-light) 0%, var(--navy) 40%, var(--navy-deep) 100%);
    font-family: "Montserrat", sans-serif; color: var(--white); overflow: hidden;
  }
  .cover__frame {
    position: absolute; inset: 18px; border: 2px solid var(--gold); pointer-events: none;
  }
  .gold-text {
    background: linear-gradient(180deg, var(--gold-light) 0%, var(--gold) 55%, var(--gold-dark) 100%);
    -webkit-background-clip: text; background-clip: text; color: transparent;
  }
  .ribbon {
    position: absolute; left: 62px; top: 72px; width: 530px; height: 30px;
    background: linear-gradient(90deg, var(--gold-dark), var(--gold-light) 50%, var(--gold-dark));
    clip-path: polygon(14px 0, 100% 0, calc(100% - 14px) 100%, 0 100%);
    color: var(--ink); font-weight: 800; font-size: 16px; letter-spacing: 0.3px;
    display: flex; align-items: center; justify-content: center;
  }
  .seal { position: absolute; left: 604px; top: 44px; width: 96px; height: 110px; }
  .title { position: absolute; left: 0; top: 112px; width: 100%; text-align: center; }
  .title__the { font-weight: 800; font-size: 44px; letter-spacing: 2px; line-height: 52px; }
  .title__lead { font-family: "Oswald", sans-serif; font-weight: 700; font-size: 118px; line-height: 124px; letter-spacing: 1px; }
  .title__main { font-weight: 900; font-size: 82px; line-height: 96px; letter-spacing: 1px; }
  .title__tail { font-weight: 800; font-size: 50px; line-height: 58px; letter-spacing: 1px; }
  .divider { position: absolute; left: 210px; top: 448px; width: 315px; height: 24px; }
  .subtitle {
    position: absolute; left: 0; top: 480px; width: 100%; text-align: center;
    color: var(--gold-light); font-weight: 700; font-size: 24px; line-height: 32px;
  }
  .hero {
    position: absolute; left: 19px; top: 550px; width: 697px; height: 395px;
    background: radial-gradient(ellipse at 50% 75%, #f1c86a 0%, #8a6a2a 14%, #1d3c7a 38%, var(--navy) 68%, var(--navy-deep) 100%);
  }
  .tagline {
    position: absolute; left: 0; top: 958px; width: 100%; text-align: center;
    font-weight: 800; font-size: 23px; line-height: 30px; letter-spacing: 0.3px;
  }
  .tagline__second { color: var(--gold-light); }
  .features {
    position: absolute; left: 46px; top: 1032px; width: 644px; height: 70px;
    display: flex; align-items: center;
  }
  .feature { flex: 1; display: flex; align-items: center; gap: 12px; }
  .feature__icon { width: 54px; height: 54px; flex: none; }
  .feature__text { font-weight: 700; font-size: 12.5px; line-height: 16px; white-space: nowrap; }
  .features__rule { width: 1px; height: 56px; background: var(--gold); margin: 0 20px; opacity: 0.7; }
  .author {
    position: absolute; left: 40px; top: 1108px; width: 655px; height: 44px;
    background: linear-gradient(90deg, var(--gold-dark), var(--gold-light) 50%, var(--gold-dark));
    clip-path: polygon(16px 0, calc(100% - 16px) 0, 100% 100%, 0 100%);
    color: var(--ink); font-weight: 800; font-size: 27px; letter-spacing: 3px;
    display: flex; align-items: center; justify-content: center;
  }
</style>
</head>
<body>
<main class="cover">
  <div class="cover__frame"></div>

  <div class="ribbon">A PRACTICAL GUIDE FOR FINANCIAL PROFESSIONALS</div>

  <svg class="seal" viewBox="0 0 96 110" aria-hidden="true">
    <defs>
      <linearGradient id="sealGold" x1="0" y1="0" x2="0" y2="1">
        <stop offset="0" stop-color="#f6d57e"/><stop offset="1" stop-color="#9c7226"/>
      </linearGradient>
    </defs>
    <circle cx="48" cy="55" r="44" fill="url(#sealGold)"/>
    <circle cx="48" cy="55" r="37" fill="#0d1f45"/>
  </svg>

  <h1 class="title">
    <div class="title__the">THE</div>
    <div class="title__lead gold-text">QUIET HOUR</div>
    <div class="title__main">SAFEGUARD</div>
    <div class="title__tail">HANDBOOK</div>
  </h1>

  <svg class="divider" viewBox="0 0 315 24">
    <line x1="0" y1="12" x2="140" y2="12" stroke="#d9a93f" stroke-width="1.5"/>
    <line x1="175" y1="12" x2="315" y2="12" stroke="#d9a93f" stroke-width="1.5"/>
    <rect x="149" y="4" width="17" height="17" rx="3" fill="none" stroke="#d9a93f" stroke-width="1.5"/>
    <rect x="153" y="11" width="9" height="7" rx="1" fill="#d9a93f"/>
    <path d="M155 11 v-2 a2.5 2.5 0 0 1 5 0 v2" fill="none" stroke="#d9a93f" stroke-width="1.3"/>
  </svg>

  <p class="subtitle">Protect Yourself and Your Family<br>in the AI Age</p>

  <div class="hero" role="img" aria-label="Illustration: a glowing gold shield with a fingerprint, a family of four in silhouette holding hands before it, a digital city skyline and circuit lines behind, with small lock and identity icons on either side"></div>

  <p class="tagline">
    <span>IT’S BETTER TO HAVE IT AND NOT NEED IT</span><br>
    <span class="tagline__second">THAN NEED IT AND NOT HAVE IT.</span>
  </p>

  <div class="features">
    <div class="feature">
      <svg class="feature__icon" viewBox="0 0 58 58">
        <circle cx="29" cy="29" r="27" fill="none" stroke="#d9a93f" stroke-width="2"/>
        <circle cx="29" cy="22" r="6" fill="#d9a93f"/>
        <path d="M18 41 a11 10 0 0 1 22 0 Z" fill="#d9a93f"/>
        <circle cx="17" cy="25" r="4" fill="#d9a93f"/>
        <circle cx="41" cy="25" r="4" fill="#d9a93f"/>
        <path d="M10 38 a7 7 0 0 1 12 -4 M48 38 a7 7 0 0 0 -12 -4" fill="none" stroke="#d9a93f" stroke-width="3"/>
      </svg>
      <div class="feature__text">FOR FINANCIAL ADVISORS,<br>PLANNERS, INSURANCE AGENTS<br>BANKERS &amp; CLIENT ADVOCATES</div>
    </div>
    <div class="features__rule"></div>
    <div class="feature">
      <svg class="feature__icon" viewBox="0 0 58 58">
        <path d="M29 4 L52 12 V30 C52 44 42 52 29 56 C16 52 6 44 6 30 V12 Z" fill="none" stroke="#d9a93f" stroke-width="2.5"/>
        <path d="M19 30 L26 37 L40 22" fill="none" stroke="#d9a93f" stroke-width="3.5" stroke-linecap="round" stroke-linejoin="round"/>
      </svg>
      <div class="feature__text">A SIMPLE, PROVEN FRAMEWORK<br>TO HELP PROTECT WHAT<br>MATTERS MOST.</div>
    </div>
  </div>

  <div class="author">YOUR NAME HERE</div>
</main>
</body>
</html>
```